Analytics/BI tech start-up seeks sharp, creative, simple, secret agent type logo & theme

"Quill 9 Dynamics" seeks a logo design/color scheme template for NYC based tech start-up of software engineers, solutions architects, and data/BI analysts. We develop reporting solutions and analytics platforms for small-medium sized businesses. We code for database, cloud, and web/mobile apps.<br/><br/>Some *very basic, limited* sketches are attached to show ideas we've had. We need a logo and color scheme that may be used for business cards, paper letterhead and envelopes, and web pages to be published at "www.quill9.dev".<br/><br/>We like the black/red, red/white, blue/black, white/black contrasts as a stating point, and prefer black background business cards, but open to anything if it feels like a good match. We are relying on the projects submitted here to take care of the creativity part of our image, which we work on logistics to launching our start-up. Something that could also be easily translated into black/white, grayscale would be appreciated as well. while log is important, we also need an icon that may be used as an app thumbnail. For font, we prefer all caps.<br/><br/>Business: Quill 9 Dynamics<br/>Slogan: If. Else. Us. / If -> Else -> Us / If - Else - Us / etc.<br/>Website: www.quill.dev<br/>Icon: [Q9] , only as a starting point<br/>Theme Ideas: Sleek, futuristic, secret agent-like tech, simple, bold color contrasts, software code related<br/><br/>Feel free to reach out to jdrevnik@mailvora.net as a contact for any questions or follow up. We look forward to seeing amazing ideas!
Updates

We would like to provide the opportunity for as many different submissions as possible.

Target Market(s)

Small business owners, entrepreneurs, financial/tech companies, freelance engineers, people in need of IT assistance to elevate business

Industry/Entity Type

It Company

Contact Information for Business Card

Individual Info: Name, Position, Phone Number 1, Phone Number 2 (optional), Fax Number, email Address.
Company Info: Name, logo, icon (optional), web site, slogan

Font styles to use
Sans Serif
Other font styles liked:
• Similar to Biome Light All Caps, Hollow Meridian type style

Requirements
Must have
• Pronounced 1 in the logo, either in the word Quill or not. Bold color contrast, one side with only logo or icon, possible web address too. Other side with all individual info plus logo, and/or icon and web address. If using uploaded files as a base, center the C more between the E and T, it is too closer to the T as is.
Nice to have
• Bolder font possibly, more square edged at ends of letters but still with minor curved corners. Icon suggested as a starting point is “[Q9]” and instead of a slogan, use "Data - Cloud - Web - Software" and the dividers don't necessary have to be hyphens.
Should not have
• Open to all creative ideas, try anything. Please come up with different logos than are in the attached files, they are meant as a starting point.

```html
<!DOCTYPE html>
<html lang="en">
<head>
<meta charset="utf-8">
<title>Quill 9 Dynamics — Business Card</title>
<link href="https://fonts.googleapis.com/css2?family=Roboto:wght@300;400;700&display=swap" rel="stylesheet">
<style>
  :root {
    --backdrop: #e8e8e8;
    --card: #363536;
    --edge: #1a7ad4;
    --accent: #1f7fd8;
    --ink: #f2f2f2;
    --rule: #8a8a8a;
    --mark: #77777a;
  }
  * { box-sizing: border-box; margin: 0; padding: 0; }
  html, body {
    width: 1200px; height: 801px; overflow: hidden;
    background: var(--backdrop);
    font-family: "Roboto", Arial, sans-serif;
  }
  .sheet {
    position: relative; width: 1200px; height: 801px;
    display: flex; align-items: center; justify-content: center; gap: 50px;
  }
  .card {
    position: relative; width: 540px; height: 309px;
    background: var(--card);
    border-bottom: 4px solid var(--edge);
    border-left: 2px solid var(--edge);
    box-shadow: 0 6px 18px rgba(0,0,0,0.18);
  }
  /* front */
  .card-front { display: flex; align-items: center; }
  .brand {
    width: 250px; padding-left: 36px;
    color: var(--accent); font-weight: 300;
    text-transform: uppercase; line-height: 1.05;
  }
  .brand-name { font-size: 40px; letter-spacing: 1px; }
  .brand-sub { font-size: 21px; letter-spacing: 3.5px; }
  .divider { width: 1px; height: 150px; background: var(--rule); }
  .details { padding-left: 24px; color: var(--ink); font-size: 15px; line-height: 1.3; }
  .person-name { color: var(--accent); font-weight: 700; font-size: 19px; }
  .person-role { font-size: 16px; margin-bottom: 10px; }
  .address { margin-bottom: 10px; }
  .contact-list { list-style: none; }
  .contact-list li { display: flex; align-items: center; gap: 9px; }
  .contact-list svg { width: 12px; height: 12px; flex: none; }
  .hl { color: var(--accent); }
  /* back */
  .card-back { display: flex; flex-direction: column; align-items: center; justify-content: center; }
  .back-mark {
    color: var(--mark); font-weight: 300; font-size: 44px;
    letter-spacing: 3px; text-transform: uppercase;
    margin-top: 10px; margin-bottom: 50px;
  }
  .back-web { color: var(--ink); font-size: 17px; letter-spacing: 3px; }
</style>
</head>
<body>
<main class="sheet">
  <section class="card card-front">
    <div class="brand">
      <div class="brand-name">Quill 9</div>
      <div class="brand-sub">Dynamics</div>
    </div>
    <div class="divider"></div>
    <div class="details">
      <div class="person-name">Dana Whitlock</div>
      <div class="person-role">Manager</div>
      <div class="address">Your address, city<br>state, ZIP 0000</div>
      <ul class="contact-list">
        <li>
          <svg viewBox="0 0 12 12"><path d="M2.5 1h2l1 2.5-1.3 1a6 6 0 0 0 3.3 3.3l1-1.3L11 7.5v2A1.5 1.5 0 0 1 9.5 11 8.5 8.5 0 0 1 1 2.5 1.5 1.5 0 0 1 2.5 1z" fill="var(--accent)"/></svg>
          212-555-0147
        </li>
        <li>
          <svg viewBox="0 0 12 12"><rect x="1" y="2.5" width="10" height="7" fill="none" stroke="var(--accent)" stroke-width="1.2"/><path d="M1 2.5l5 4 5-4" fill="none" stroke="var(--accent)" stroke-width="1.2"/></svg>
          hello@quill9.dev
        </li>
        <li>
          <svg viewBox="0 0 12 12"><circle cx="6" cy="6" r="5" fill="none" stroke="var(--accent)" stroke-width="1.2"/><path d="M1 6h10M6 1c-2.5 3-2.5 7 0 10M6 1c2.5 3 2.5 7 0 10" fill="none" stroke="var(--accent)" stroke-width="1"/></svg>
          <span>www.<span class="hl">quill9</span>.dev</span>
        </li>
      </ul>
    </div>
  </section>

  <section class="card card-back">
    <div class="back-mark">Quill 9 Dynamics</div>
    <div class="back-web">www.<span class="hl">quill9</span>.dev</div>
  </section>
</main>
</body>
</html>
```